Flyer

I am a qualified accountant and I need a flyer to promote my business when networking

My services include
Management Accounts, Financial Accounts, Day to Day Bookkeeping services, business start up assistance
I will produce and submit Self Assessment Tax Returns, Annual Accounts, VAT tax returns, Payroll and PAYE

I attach my business card design so that there is some continuity if you think it appropiate.

Size A3 is preferred, please.

Sorry, I mean't Size A5 is preferred.

A5 please

Free initial consultations and advice.                                   

Business

```html
<!DOCTYPE html>
<html lang="en">
<head>
<meta charset="utf-8">
<title>Clare Morton Accounting – Flyer</title>
<link href="https://fonts.googleapis.com/css2?family=Cinzel:wght@400;600&family=PT+Sans:wght@400;700&family=PT+Sans+Narrow:wght@700&display=swap" rel="stylesheet">
<style>
  :root {
    --page-bg: #e9e7e3;
    --paper: #ffffff;
    --green-deep: #1d7330;
    --green-mid: #2f8f3c;
    --lime: #a8cd3a;
    --lime-soft: #cfe06a;
    --orange: #ec5a24;
    --ink: #3a3a3a;
    --white: #ffffff;
  }
  * { box-sizing: border-box; margin: 0; padding: 0; }
  html, body { width: 932px; height: 1200px; overflow: hidden; background: var(--page-bg); }
  .flyer {
    position: absolute; left: 42px; top: 0;
    width: 848px; height: 1200px;
    background: var(--paper);
    overflow: hidden;
    font-family: "PT Sans", sans-serif;
  }
  .flyer-shapes { position: absolute; inset: 0; width: 100%; height: 100%; }

  .brand { position: absolute; left: 0; right: 0; top: 60px; text-align: center; }
  .brand-mark {
    display: block; width: 62px; height: 62px; margin: 0 auto 30px;
    border-radius: 50%; background: var(--lime);
  }
  .brand-name {
    font-family: "Cinzel", serif; font-weight: 400;
    font-size: 44px; letter-spacing: 1px; color: var(--ink); line-height: 1;
  }
  .brand-tagline { font-size: 27px; color: var(--ink); margin-top: 10px; line-height: 1; }

  .services { position: absolute; left: 56px; top: 474px; width: 424px; color: var(--white); }
  .services-title { font-size: 35px; font-weight: 700; color: var(--lime); margin-bottom: 24px; line-height: 1.1; }
  .services-list { list-style: none; }
  .services-list li {
    position: relative; padding-left: 49px;
    font-size: 24px; line-height: 42px; margin-bottom: 2px;
  }
  .tick { position: absolute; left: 5px; top: 10px; width: 24px; height: 24px; }

  .profile-name {
    position: absolute; left: 536px; width: 230px; top: 484px;
    text-align: center; color: var(--white);
    font-family: "Cinzel", serif; font-size: 26px; line-height: 32px;
  }
  .photo-frame {
    position: absolute; width: 206px; height: 252px;
    background: var(--white); padding: 10px;
    box-shadow: 0 4px 10px rgba(0,0,0,.35);
  }
  .photo-frame.back { left: 540px; top: 570px; transform: rotate(6deg); }
  .photo-frame.front { left: 524px; top: 582px; transform: rotate(-10deg); }
  .photo {
    width: 100%; height: 100%;
    background: linear-gradient(160deg, #d9c7b1 0%, #b88e6c 55%, #4b3f3a 100%);
  }

  .offer-badge {
    position: absolute; left: 536px; top: 916px;
    width: 248px; height: 248px; border-radius: 50%;
    background: var(--orange); border: 4px solid var(--white);
    box-shadow: 0 3px 8px rgba(0,0,0,.25);
    display: flex; align-items: center; justify-content: center;
    text-align: center; color: var(--white);
    font-weight: 700; font-size: 33px; line-height: 41px;
  }

  .contact { position: absolute; left: 50px; top: 1056px; color: var(--ink); }
  .contact-email { font-size: 22px; font-weight: 700; }
  .contact-phone {
    font-family: "PT Sans Narrow", sans-serif; font-weight: 700;
    font-size: 54px; margin-top: 18px; line-height: 1;
  }
</style>
</head>
<body>
  <main class="flyer">
    <svg class="flyer-shapes" viewBox="0 0 486 688" preserveAspectRatio="none" aria-hidden="true">
      <defs>
        <linearGradient id="greenBody" x1="0" y1="0" x2="1" y2="1">
          <stop offset="0" stop-color="#2f8f3c"/>
          <stop offset="1" stop-color="#1d7330"/>
        </linearGradient>
      </defs>
      <path d="M0,118 C120,168 260,214 486,206 L486,224 C260,230 120,190 0,140 Z" fill="#cfe06a"/>
      <path d="M0,128 C120,178 260,220 486,214 L486,226 C260,232 120,194 0,142 Z" fill="#a8cd3a"/>
      <path d="M0,140 C120,190 250,232 486,226 L486,612 C360,590 150,545 0,550 Z" fill="url(#greenBody)"/>
      <path d="M0,150 C120,198 250,238 486,234" fill="none" stroke="#ffffff" stroke-width="1.2" opacity=".8"/>
      <path d="M0,550 C150,545 360,590 486,612 L486,642 C380,612 200,566 0,562 Z" fill="#a8cd3a"/>
      <path d="M0,562 C200,566 380,612 486,642 L486,650 C380,622 200,574 0,570 Z" fill="#cfe06a"/>
      <path d="M0,546 C150,540 360,584 486,606" fill="none" stroke="#ffffff" stroke-width="1.2" opacity=".8"/>
    </svg>

    <header class="brand">
      <span class="brand-mark"></span>
      <h1 class="brand-name">Clare Morton Accounting</h1>
      <p class="brand-tagline">Making Accounts look easy</p>
    </header>

    <section class="services">
      <h2 class="services-title">My Services Include</h2>
      <ul class="services-list">
        <li><svg class="tick" viewBox="0 0 24 24"><rect x="1" y="3" width="18" height="18" fill="#fff"/><path d="M5 12 l5 5 L23 2" fill="none" stroke="#a8cd3a" stroke-width="3.5"/></svg>Management Accounts</li>
        <li><svg class="tick" viewBox="0 0 24 24"><rect x="1" y="3" width="18" height="18" fill="#fff"/><path d="M5 12 l5 5 L23 2" fill="none" stroke="#a8cd3a" stroke-width="3.5"/></svg>Financial Accounts</li>
        <li><svg class="tick" viewBox="0 0 24 24"><rect x="1" y="3" width="18" height="18" fill="#fff"/><path d="M5 12 l5 5 L23 2" fill="none" stroke="#a8cd3a" stroke-width="3.5"/></svg>Budgeting</li>
        <li><svg class="tick" viewBox="0 0 24 24"><rect x="1" y="3" width="18" height="18" fill="#fff"/><path d="M5 12 l5 5 L23 2" fill="none" stroke="#a8cd3a" stroke-width="3.5"/></svg>Day to Day Bookkeeping Services</li>
        <li><svg class="tick" viewBox="0 0 24 24"><rect x="1" y="3" width="18" height="18" fill="#fff"/><path d="M5 12 l5 5 L23 2" fill="none" stroke="#a8cd3a" stroke-width="3.5"/></svg>business start up assistance</li>
        <li><svg class="tick" viewBox="0 0 24 24"><rect x="1" y="3" width="18" height="18" fill="#fff"/><path d="M5 12 l5 5 L23 2" fill="none" stroke="#a8cd3a" stroke-width="3.5"/></svg>I will produce and submit Self<br>Assessment Tax Returns, Annual<br>Accounts, VAT tax returns, Payroll<br>and PAYE</li>
      </ul>
    </section>

    <p class="profile-name">Clare Morton<br>ACMA, CGMA</p>
    <div class="photo-frame back"></div>
    <div class="photo-frame front"><div class="photo" role="img" aria-label="Portrait photograph of the accountant"></div></div>

    <div class="offer-badge">Free<br>initial<br>consultations<br>and advice</div>

    <footer class="contact">
      <p class="contact-email">Email: clare@claremortonaccounting.com</p>
      <p class="contact-phone">Call : 07700 900481</p>
    </footer>
  </main>
</body>
</html>
```